Text heavy poster for university audience

I have developed a set of standards for online teaching that need to be turned into a post format. The project has a logo which should be incorporated. Most of the designing will be in terms of text layout. The logo (two versions - higher quality files available) and the a sample of standards (as image - word version available; the example is one third of standards) are attached. Design that can be adapted to brochure format would be great. (Brochure adaption will be paid separately via another project to be opened here). More details available here: http://www.brightmeadowhub.org
Updates

Dear all,

The URL for the site needs to be include in the design - either as footer or under logo:
<http://www.brightmeadowhub.org>

Sorry for late notice

Target Market(s)

The are university staff

Industry/Entity Type

University

Font styles to use
Serif
Sans Serif

Requirements
Must have
• The text in the "required" attachment must be included; but for initial draft feel free to restrict your design to "sample" attachment
The green from the Logo (PANTONE 17-5641 Emerald) should be the foundation of the colour palette.
Nice to have
• The collaborators as named here: http://www.brightmeadowhub.org/collaborators/
My preferred find is helvetica neue, but similar can be used
Should not have
• Decorative fonts

```html
<!DOCTYPE html>
<html lang="en">
<head>
<meta charset="utf-8">
<title>Brightmeadow Online Standards – Poster</title>
<link rel="stylesheet" href="https://fonts.googleapis.com/css2?family=Roboto:ital,wght@0,400;0,700;0,900;1,700;1,900&display=swap">
<style>
:root{
  --emerald:#1f9b77;
  --silver-light:#f4f4f4;
  --silver:#d9d9da;
  --panel:#5e5e60;
  --panel-text:#b9b9ba;
  --ink:#3a3a3a;
  --ink-soft:#555;
  --page:#ffffff;
}
*{margin:0;padding:0;box-sizing:border-box}
html,body{width:1200px;height:1000px;overflow:hidden;background:var(--page)}
body{font-family:"Roboto",Arial,sans-serif;color:var(--ink);position:relative}
.poster{position:absolute;left:272px;top:15px;width:680px;height:958px;overflow:hidden;
  background:linear-gradient(100deg,var(--silver-light) 0%,#e2e2e3 30%,#f6f6f6 55%,var(--silver) 100%);
  box-shadow:3px 6px 10px rgba(0,0,0,.35)}
.poster-art{position:absolute;left:0;top:0}
.watermark{position:absolute;left:-362px;top:505px;width:800px;height:110px;line-height:110px;
  transform:rotate(-90deg);transform-origin:center;
  font-size:108px;font-weight:900;font-style:italic;letter-spacing:14px;color:rgba(255,255,255,.7);text-align:center;white-space:nowrap}
.brand{position:absolute;left:22px;top:17px;display:flex;align-items:center;gap:10px}
.brand-mark{width:44px;height:44px;background:#fff}
.brand-name{color:#fff;font-weight:700;font-size:13.5px;line-height:16px;letter-spacing:.2px}
.site-url{position:absolute;left:266px;top:8px;color:#fff;font-size:21px;letter-spacing:1.6px;font-weight:400}
.panel{position:absolute;left:421px;top:55px;width:252px;height:888px;background:var(--panel)}
.panel-title{position:absolute;left:421px;top:72px;width:252px;text-align:center;color:var(--emerald);
  font-weight:900;font-style:italic;font-size:13px}
.names{position:absolute;top:93px;list-style:none;font-size:4.4px;line-height:9.5px;color:var(--panel-text);white-space:nowrap}
.names-left{left:425px;width:115px;text-align:right}
.names-right{left:552px;width:118px;text-align:left}
.section{position:absolute;width:330px}
.section-one{left:80px;top:128px}
.section-two{left:80px;top:490px}
.section-three{left:27px;top:652px;width:385px}
.section-title{color:var(--emerald);font-size:12.5px;font-weight:700;line-height:14px}
.section-intro{font-size:6.6px;line-height:8px;color:var(--ink-soft);margin-bottom:8px}
.section-intro b{color:#333;font-weight:700;font-size:7.4px}
.standard{margin-bottom:8px;padding-left:2px}
.standard h3{font-size:6.2px;line-height:8px;font-style:italic;font-weight:900;text-transform:uppercase;color:#4a4a4a}
.standard h3 .wrap{padding-left:8px}
.standard ul{list-style:none;padding-left:6px}
.standard li{font-size:4.8px;line-height:6.6px;color:var(--ink-soft)}
.standard li::before{content:"• "}
.standard li b{font-weight:700;color:#444}
.section-three .standard{margin-bottom:7px}
.divider{position:absolute;height:1px;background:#c4c4c4}
</style>
</head>
<body>
<div class="poster">
  <div class="watermark" aria-hidden="true">STANDARDS</div>

  <div class="panel"></div>

  <svg class="poster-art" width="680" height="958" viewBox="0 0 680 958" aria-hidden="true">
    <path d="M0 0H680V50C520 52 300 62 0 92Z" fill="var(--emerald)"/>
    <path d="M0 92C300 62 520 52 680 50V62C520 62 300 72 0 104Z" fill="#ffffff" opacity=".9"/>
    <path d="M0 104C300 72 520 62 680 62V70C520 70 300 80 0 114Z" fill="#b8b8ba" opacity=".7"/>
    <path d="M0 930C250 926 480 922 680 918V958H0Z" fill="#c9c9ca"/>
    <path d="M0 940C250 936 480 932 680 930V958H0Z" fill="var(--emerald)"/>
  </svg>

  <div class="brand">
    <span class="brand-mark" aria-hidden="true"></span>
    <div class="brand-name">BRIGHTMEADOW<br>ONLINE<br>STANDARDS</div>
  </div>
  <div class="site-url">WWW.BRIGHTMEADOWHUB.ORG</div>

  <div class="panel-title">Dana Whitcombe and Collaborators</div>

  <ul class="names names-left">
    <li>Abbott, Carla (Northgate)</li><li>Adair, Tristan (Harbour University)</li><li>Ainsley, Maren (Bayford University)</li><li>Alcott, Dean (Clearpath Education)</li><li>Arden, Phoebe (Ridgeway)</li><li>Ashby, Colin (Eastvale)</li><li>Atwell, Rhonda (Summit University)</li><li>Avery, Nolan (Eastvale)</li><li>Baird, Lena (Kestrel University)</li><li>Balfour, Grant (Eastvale)</li><li>Barlow, Hazel (Summit University)</li><li>Beckett, Ivan (Northgate)</li><li>Benning, Clara (Northgate)</li><li>Blaine, Oscar (Ridgeway)</li><li>Bolton, Frances (Harbour University)</li><li>Bramley, Neil (Eastvale)</li><li>Brennan, Tessa (Eastvale)</li><li>Brook, Alina (Ridgeway)</li><li>Burgess, Leon (Kestrel University)</li><li>Calder, Wendy (Northgate)</li><li>Carver, Ronan (Ridgeway)</li><li>Castell, Miriam (Harbour University)</li><li>Chalmers, Gwen (Ridgeway)</li><li>Chaplin, Reid (Ridgeway)</li><li>Chisholm, Ada (Westmoor)</li><li>Clifton, Bryce (Lakeside University)</li><li>Colby, Naomi (Northgate)</li><li>Corbett, Elliot (Summit University)</li><li>Cosgrove, Hilda (Lakeside University)</li><li>Crane, Darcy (Northgate)</li><li>Crowther, Milo (Northgate)</li><li>Dalby, Fern (Westmoor)</li><li>Darrow, Quentin (Ridgeway)</li><li>Davenport, Iris (Lakeside University)</li><li>Delaney, Rufus (Kestrel University)</li><li>Denholm, Greta (Northgate)</li><li>Dorsey, Alan (Kestrel University)</li><li>Drayton, Sylvie (Lakeside University)</li><li>Durant, Hugo (Ridgeway)</li><li>Eastwood, Mabel (Northgate)</li><li>Elkins, Judd (Harbour University)</li><li>Emsley, Noreen (Summit University)</li><li>Everard, Troy (Westmoor)</li><li>Fairley, Dina (Eastvale)</li><li>Farrant, Cole (Westmoor)</li><li>Fenwick, Lottie (Summit University)</li><li>Finlay, Ross (Ridgeway)</li><li>Fletcher, Anouk (Bayford University)</li><li>Forsyth, Gideon (Ridgeway)</li><li>Fraser, Ilse (Lakeside University)</li><li>Galloway, Brent (Northgate)</li><li>Garner, Petra (Northgate)</li><li>Gifford, Owen (Northgate)</li><li>Goddard, Leah (Summit University)</li><li>Gorman, Tobias (Summit University)</li><li>Granger, Edith (Lakeside University)</li><li>Grayson, Vance (Kestrel University)</li><li>Hadley, Ruth (Eastvale)</li><li>Halloran, Jude (Ridgeway)</li><li>Harcourt, Vera (Ridgeway)</li><li>Hartley, Boyd (Kestrel University)</li><li>Haskins, Nora (Ridgeway)</li><li>Hawley, Simone (Harbour University)</li><li>Hayward, Clint (Northgate)</li><li>Heston, Marla (Lakeside University)</li><li>Hollis, Ward (Eastvale)</li><li>Horton, Bianca (Kestrel University)</li><li>Howell, Linus (Northgate)</li><li>Ingram, Delia (Eastvale)</li><li>Irving, Conrad (Ridgeway)</li><li>Ivers, Kendra (Ridgeway)</li><li>Jarvis, Malcolm (Kestrel University)</li><li>Jeffers, Opal (Kestrel University)</li><li>Jennings, Rory (Eastvale)</li><li>Kearney, Thea (Lakeside University)</li><li>Keeling, Amos (Northgate)</li><li>Kendrick, Lydia (Harbour University)</li><li>Kerwin, Barnaby (Eastvale)</li><li>Kingsley, Faye (Harbour University)</li><li>Kirby, Desmond (Summit University)</li><li>Lambert, Ines (Lakeside University)</li><li>Langford, Jasper (Kestrel University)</li><li>Larkin, Meryl (Kestrel University)</li><li>Lawton, Silas (Harbour University)</li><li>Leland, Corinne (Westmoor)</li><li>Linden, Reuben (Ridgeway)</li>
  </ul>
  <ul class="names names-right">
    <li>Lockhart, Aileen (Lakeside University)</li><li>Lowry, Dexter (Eastvale)</li><li>Lyall, Hester (Kestrel University)</li><li>Maddox, Ferris (Lakeside University)</li><li>Malone, Ginny (Harbour University)</li><li>Manning, Tobin (Eastvale)</li><li>Marchant, Lorna (Kestrel University)</li><li>Mercer, Alden (Lakeside University)</li><li>Merritt, Joy (Ridgeway)</li><li>Milburn, Cecil (Lakeside University)</li><li>Moffat, Renée (Lakeside University)</li><li>Molloy, Garth (Ridgeway)</li><li>Montague, Elsie (Kestrel University)</li><li>Morley, Anand (Ridgeway)</li><li>Murdoch, Paige (Summit University)</li><li>Nash, Raymond (Summit University)</li><li>Neville, Wren (Kestrel University)</li><li>Newell, Harlan (Ridgeway)</li><li>Norwood, Celia (Ridgeway)</li><li>Oakes, Dorian (Westmoor)</li><li>Ogden, Mina (Northgate)</li><li>Orchard, Lyle (Lakeside University)</li><li>Osgood, Fleur (Eastvale)</li><li>Otway, Bruno (Westmoor)</li><li>Paget, Estelle (Lakeside University)</li><li>Palmer, Jonah (Westmoor)</li><li>Parrish, Ottilie (Clearpath Education)</li><li>Paxton, Myles (Eastvale)</li><li>Pembroke, Alma (Northgate)</li><li>Penrose, Kit (Lakeside University)</li><li>Perrin, Ida (Lakeside University)</li><li>Pickard, Lowell (Westmoor)</li><li>Plummer, Enid (Northgate)</li><li>Prescott, Wade (Eastvale)</li><li>Quarles, Della (Harbour University)</li><li>Quayle, Rhys (Eastvale)</li><li>Radford, Ursula (Ridgeway)</li><li>Ramsay, Idris (Eastvale)</li><li>Rathbone, Coral (Westmoor)</li><li>Redmond, Ezra (Bayford University)</li><li>Renshaw, Mae (Eastvale)</li><li>Ridley, Arlo (Ridgeway)</li><li>Rigby, Nell (Lakeside University)</li><li>Rowntree, Felix (Ridgeway)</li><li>Rushford, Imogen (Summit University)</li><li>Sadler, Keaton (Lakeside University)</li><li>Salter, Beryl (Summit University)</li><li>Sawyer, Declan (Westmoor)</li><li>Seaton, Jolene (Kestrel University)</li><li>Selby, Otis (Eastvale)</li><li>Sheridan, Vivian (Harbour University)</li><li>Shipley, Lorcan (Ridgeway)</li><li>Sinclair, Maeve (Lakeside University)</li><li>Slater, Brandon (Ridgeway)</li><li>Spalding, Rosalind (Kestrel University)</li><li>Stafford, Gus (Northgate)</li><li>Stirling, Aurora (Eastvale)</li><li>Stroud, Ellis (Eastvale)</li><li>Sutcliffe, Tamsin (Eastvale)</li><li>Swann, Lucien (Northgate)</li><li>Talbot, Rowena (Lakeside University)</li><li>Tanner, Hollis (Eastvale)</li><li>Thackeray, Ilona (Lakeside University)</li><li>Thorne, Emmett (Kestrel University)</li><li>Tilley, Beatrix (Lakeside University)</li><li>Townsend, Kirk (Summit University)</li><li>Tremaine, Olive (Bayford University)</li><li>Truscott, Wynn (Lakeside University)</li><li>Underhill, Greer (Kestrel University)</li><li>Upton, Rafe (Ridgeway)</li><li>Vance, Marisol (Eastvale)</li><li>Varley, Ned (Westmoor)</li><li>Vickers, Opal (Northgate)</li><li>Wadsworth, Cyril (Bayford University)</li><li>Waller, Henrietta (Bayford University)</li><li>Warwick, Dale (Ridgeway)</li><li>Webber, Sabine (Summit University)</li><li>Wetherby, Lance (Lakeside University)</li><li>Whitfield, Petula (Eastvale)</li><li>Wickham, Gordon (Kestrel University)</li><li>Winslow, Hattie (Ridgeway)</li><li>Winthrop, Ansel (Eastvale)</li><li>Worsley, Cassia (Bayford University)</li><li>Wyatt, Fletcher (Northgate)</li><li>Yardley, Isolde (Summit University)</li><li>Yates, Royce (Kestrel University)</li><li>Young, Philippa (Summit University)</li><li>Zeller, Maxwell (Kestrel University)</li>
  </ul>

  <section class="section section-one">
    <h2 class="section-title">ONE: STUDENTS</h2>
    <p class="section-intro">Students are supported in their online learning with a quality <b>curriculum</b> [1-4],<br>opportunities for interaction with peers and staff [5&amp;6], and appropriate <b>support</b> [7&amp;8].</p>
    <article class="standard"><h3>1. Curriculum materials are aligned, available and engaging</h3><ul><li><b>Threshold</b> - The necessary materials are constructively aligned and available online</li><li><b>Good</b> - The materials are provided using a variety of media to engage students and support diversity</li><li><b>Excellent</b></li></ul></article>
    <article class="standard"><h3>2. Learning activities are aligned, available and engaging</h3><ul><li><b>Threshold</b> - Constructively aligned learning activities are available online</li><li><b>Good</b> - Learning activities use a variety of appropriate technologies to engage students and support diversity</li><li><b>Excellent</b></li></ul></article>
    <article class="standard"><h3>3. Assessment tasks are aligned, available and engaging</h3><ul><li><b>Threshold</b> - Constructively aligned assessment tasks are available online</li><li><b>Good</b> - Assessment tasks use a variety of appropriate technologies to engage students and support diversity</li><li><b>Excellent</b></li></ul></article>
    <article class="standard"><h3>4. Students are provided with timely, improvement focused formative feedback</h3><ul><li><b>Threshold</b> - Appropriate technologies are used to provide students with formative feedback in a timely manner</li><li><b>Good</b> - Feedback is provided in a variety of media to engage students and support diversity</li><li><b>Excellent</b></li></ul></article>
    <article class="standard"><h3>5. Students are provided with opportunities to interact with peers</h3><ul><li><b>Threshold</b> - There are opportunities for social interaction</li><li><b>Good</b> - There are opportunities for learning-focused interaction</li><li><b>Excellent</b></li></ul></article>
    <article class="standard"><h3>6. Students are provided with opportunities to interact with staff</h3><ul><li><b>Threshold</b> - Staff are provided with opportunities to answer student queries</li><li><b>Good</b> - Staff are provided with opportunities to be active participants in learning-focused interactions</li><li><b>Excellent</b></li></ul></article>
    <article class="standard"><h3>7. Students are provided with appropriate learning support</h3><ul><li><b>Threshold</b> - Appropriate, up-to-date and reliable learning guides and resources are provided online</li><li><b>Good</b> - A range of appropriate, up-to-date and reliable learning skills workshops are available</li><li><b>Excellent</b></li></ul></article>
    <article class="standard"><h3>8. Students are supported in their use of educational technology</h3><ul><li><b>Threshold</b> - Appropriate, up-to-date and reliable technological guides and resources are provided online</li><li><b>Good</b> - Appropriate, timely and reliable asynchronous technological support is available</li><li><b>Excellent</b></li></ul></article>
  </section>

  <div class="divider" style="left:80px;top:476px;width:325px"></div>

  <section class="section section-two">
    <h2 class="section-title">TWO: STAFF</h2>
    <p class="section-intro">Staff are supported in their online teaching with quality professional<br>development [9], resourcing [10] and technical support [11].</p>
    <article class="standard"><h3>9. Staff are provided with quality professional development in online education</h3><ul><li><b>Threshold</b> - A range of appropriate, up-to-date and informative professional development activities are available to staff</li><li><b>Good</b> - The organisation requires staff to engage in continued professional development relevant to online education</li><li><b>Excellent</b></li></ul></article>
    <article class="standard"><h3>10. Online education is recognised in workload</h3><ul><li><b>Threshold</b> - Online teaching is recognised in workload</li><li><b>Good</b> - Online unit development is recognised in workload</li><li><b>Excellent</b></li></ul></article>
    <article class="standard"><h3>11. Staff are supported in their use of educational technology</h3><ul><li><b>Threshold</b> - Appropriate, up-to-date and reliable technological guides and resources are provided online</li><li><b>Good</b> - Appropriate, timely and reliable asynchronous technological support is available</li><li><b>Excellent</b></li></ul></article>
  </section>

  <div class="divider" style="left:27px;top:642px;width:378px"></div>

  <section class="section section-three">
    <h2 class="section-title">THREE: ORGANISATION</h2>
    <p class="section-intro">The organisation supports online education through the provision of<br>quality leadership [12-13], infrastructure [14] and evaluation [15-17]</p>
    <article class="standard"><h3>12. The organisation provides strategic leadership in online education</h3><ul><li><b>Threshold</b> - The organisation has a clearly articulated strategic position on online education</li><li><b>Good</b> - An appropriate member of the executive has explicit responsibility for online education</li><li><b>Excellent</b></li></ul></article>
    <article class="standard"><h3>13. The organisation employs a systematic approach to resource allocation in online education</h3><ul><li><b>Threshold</b> - There is a systematic approach to resource allocation</li><li><b>Good</b> - There is systematic approach with formal criteria that are widely available</li><li><b>Excellent</b></li></ul></article>
    <article class="standard"><h3>14. The organisation maintains and supports a quality learning platform for delivering<br><span class="wrap">online education</span></h3><ul><li><b>Threshold</b> - The organisation maintains and supports an appropriate learning platform</li><li><b>Good</b> - The learning platform provided is fit for purpose, scalable and reliable</li><li><b>Excellent</b></li></ul></article>
    <article class="standard"><h3>15. The organisation has a process for evaluating and improving student satisfaction<br><span class="wrap">with online education</span></h3><ul><li><b>Threshold</b> - The organisation has a systematic process for evaluating and improving student satisfaction with online education</li><li><b>Good</b> - The organisation has a systematic process for improving student learning outcomes and satisfaction with online education and communicating improvements to students</li><li><b>Excellent</b></li></ul></article>
    <article class="standard"><h3>16. The organisation has a process for evaluating and improving training and support for staff</h3><ul><li><b>Threshold</b> - The organisation has a systematic process for evaluating and improving staff training and support</li><li><b>Good</b> - The organisation has a systematic process for improving staff training and support and communicating improvements to staff</li><li><b>Excellent</b></li></ul></article>
    <article class="standard"><h3>17. The organisation has a process for evaluating and improving infrastructure</h3><ul><li><b>Threshold</b> - The organisation has a systematic process for evaluating and improving infrastructure</li><li><b>Good</b> - The organisation has a systematic process for improving infrastructure and communicating improvements to stakeholders</li><li><b>Excellent</b></li></ul></article>
  </section>
</div>
</body>
</html>
```